National Chemical Line for Homeowners Needs a Logo & Label Design.

We need a logo and label design for a New National Chemical Company that is Private Labeling/Creating Cleaning Chemicals for Homeowners to use themselves. These chemicals will be used to clean carpets, hard surfaces, remove cat & dog stains and odors and many other products to come.
The first product will be for homeowners to remove cat & dog stains and odors from their carpets. We would like the label for the front and back of a 32 oz. white spray bottle. Go to www.brellowsupply.example and reference Part# 41KPL7.
We want the bottle/label to stand out on the grocery store shelves. We want it to be simple to read, eye catching, have a simple name and explain what the product does . The back of the bottle will have directions, caution statements, etc.
The Name of our Company is Vanta Meridian. It does have a trademark. We want the word "Vanta" to stand out and the word "meridian to only be present, that way the word Vanta will gain traction with the customer.
We want the color scheme to be Pinks & Blues.

```html
<!DOCTYPE html>
<html lang="en">
<head>
<meta charset="utf-8">
<title>Vanta Meridian – Cat &amp; Dog Stains Remover Label</title>
<link href="https://fonts.googleapis.com/css2?family=Barlow:wght@400;600;700&display=swap" rel="stylesheet">
<style>
  :root {
    --page: #ffffff;
    --cyan: #4ef8f5;
    --aqua: #a6eef0;
    --sky: #2a9de8;
    --pink: #f4a6dc;
    --purple: #7a3fd0;
    --brand-blue: #0a9fe3;
    --band-pink: #e23a86;
    --band-pink-light: #f05ea4;
    --white: #ffffff;
    --cat-grey: #8d8f96;
    --cat-grey-dark: #5e6068;
    --dog-brown: #b8703f;
    --dog-brown-dark: #8a4a24;
  }
  * { box-sizing: border-box; margin: 0; padding: 0; }
  html, body {
    width: 1200px; height: 1200px; overflow: hidden;
    background: var(--page);
    font-family: "Barlow", sans-serif;
  }
  .canvas { position: relative; width: 1200px; height: 1200px; }

  .label {
    position: absolute; left: 280px; top: 210px;
    width: 640px; height: 780px;
    border-radius: 50% 50% 7% 7% / 20% 20% 4% 4%;
    overflow: hidden;
    background:
      radial-gradient(ellipse 60% 45% at 30% 12%, var(--cyan) 0%, rgba(78,248,245,0) 100%),
      radial-gradient(ellipse 50% 40% at 95% 58%, var(--pink) 0%, rgba(244,166,220,0) 100%),
      radial-gradient(ellipse 45% 40% at 0% 70%, var(--sky) 0%, rgba(42,157,232,0) 100%),
      radial-gradient(ellipse 55% 35% at 45% 100%, var(--purple) 0%, rgba(122,63,208,0) 100%),
      linear-gradient(180deg, var(--cyan) 0%, var(--aqua) 45%, #c9b7ec 75%, var(--purple) 100%);
  }

  .brand { position: absolute; left: 0; right: 0; top: 130px; text-align: center; }
  .brand-name {
    display: block;
    font-weight: 700; font-size: 168px; line-height: 1;
    color: var(--brand-blue); letter-spacing: -2px;
  }
  .brand-sub {
    display: block; margin-top: 6px;
    font-weight: 600; font-size: 20px; letter-spacing: 5px;
    text-transform: uppercase; color: var(--brand-blue);
  }

  .photo { position: absolute; }
  .photo-cat {
    left: 50px; top: 420px; width: 230px; height: 360px;
    border-radius: 46% 46% 0 0 / 30% 30% 0 0;
    background: linear-gradient(180deg, var(--cat-grey) 0%, var(--cat-grey-dark) 100%);
  }
  .photo-dog {
    left: 290px; top: 340px; width: 310px; height: 440px;
    border-radius: 48% 48% 0 0 / 34% 34% 0 0;
    background: linear-gradient(180deg, var(--dog-brown) 0%, var(--dog-brown-dark) 100%);
  }

  .band {
    position: absolute; left: -30px; top: 570px;
    width: 720px; height: 66px;
    transform: rotate(-9deg);
    background: linear-gradient(90deg, var(--band-pink) 0%, var(--band-pink-light) 100%);
    display: flex; align-items: center; justify-content: center;
  }
  .band-text {
    color: var(--white); font-weight: 700; font-size: 36px;
    letter-spacing: 3px; text-transform: uppercase;
  }

  .volume {
    position: absolute; left: 72px; top: 688px;
    color: var(--white); font-weight: 400; font-size: 34px;
  }
  .claim {
    position: absolute; left: 465px; top: 684px;
    color: var(--white); font-weight: 400; font-size: 19px;
    line-height: 1.1; text-align: center; text-transform: uppercase;
  }
</style>
</head>
<body>
<main class="canvas">
  <section class="label">
    <div class="brand">
      <span class="brand-name">Vanta</span>
      <span class="brand-sub">meridian</span>
    </div>
    <div class="photo photo-cat" role="img" aria-label="Photo of a smiling grey fold-eared cat"></div>
    <div class="photo photo-dog" role="img" aria-label="Photo of a fluffy apricot poodle puppy"></div>
    <div class="band"><span class="band-text">Cat &amp; Dog Stains Remover</span></div>
    <p class="volume">32 oz</p>
    <p class="claim">Bleach<br>Free</p>
  </section>
</main>
</body>
</html>
```